Customs House descriptive business cards

We require a two-sided business card that has a simple yet elegant design. We want to be able to promote our services as a customs house. This card should include our logo, contact info and services offered with the logo being on one side and the contact info and services on the flip side

Target Market(s)

Importers / exporters to and from the Bahamas

Industry/Entity Type

Logistics

Contact Information for Business Card

The front side of the card could have the logo and the flip side should have the other relevant info

Font styles to use
Serif

Colors

Designer to choose colors to be used in the design.

Requirements
Must have
• (Harbourline Agents Ltd) Logo, address and contact info also services:
• import customs clearance, Delivery & HAndling services,Florida pickups, Export packing & Crating Services, export customs clearance, Consulting

```html
<!DOCTYPE html>
<html lang="en">
<head>
<meta charset="utf-8">
<title>Harbourline Agents Ltd — Business Card</title>
<link rel="stylesheet" href="https://fonts.googleapis.com/css2?family=Cinzel:wght@600&family=Poppins:wght@400;600;700&display=swap">
<style>
  :root {
    --bg: #e6e8eb;
    --blue-deep: #1660b8;
    --blue-mid: #1f7fd0;
    --blue-light: #3a9ee4;
    --grey-wave: #c9ccd1;
    --white: #ffffff;
    --ink-dark: #2b2f36;
  }
  * { margin: 0; padding: 0; box-sizing: border-box; }
  html, body { width: 1200px; height: 870px; overflow: hidden; }
  body {
    background: var(--bg);
    font-family: "Poppins", Arial, sans-serif;
    position: relative;
  }
  .card {
    position: absolute;
    top: 280px;
    width: 540px;
    height: 310px;
    border-radius: 18px;
    overflow: hidden;
    box-shadow: 0 6px 20px rgba(0,0,0,.12);
  }
  .card--contact { left: 45px; background: var(--white); }
  .card--brand {
    left: 615px;
    background: linear-gradient(135deg, var(--blue-deep) 0%, var(--blue-mid) 55%, var(--blue-light) 100%);
    color: var(--white);
  }
  .card__waves { position: absolute; inset: 0; width: 100%; height: 100%; }

  .person { position: absolute; left: 30px; top: 30px; }
  .person::before {
    content: ""; position: absolute; left: -14px; top: 2px;
    width: 4px; height: 16px; background: var(--blue-mid);
  }
  .person__name { font-weight: 700; font-size: 15px; color: var(--blue-deep); letter-spacing: .3px; }
  .person__role { font-size: 9px; color: var(--ink-dark); letter-spacing: .4px; margin-top: 2px; }

  .brand-name {
    font-family: "Cinzel", Georgia, serif;
    font-weight: 600;
    text-align: center;
    line-height: 1.15;
  }
  .card--contact .brand-name {
    position: absolute; right: 28px; top: 34px; width: 200px;
    font-size: 18px; color: var(--blue-deep);
  }
  .brand-dot {
    display: block; width: 38px; height: 38px; border-radius: 50%;
    margin: 0 auto 8px; background: var(--blue-mid);
  }

  .contact-list { position: absolute; left: 30px; top: 168px; list-style: none; color: var(--white); }
  .contact-list li { display: flex; align-items: center; gap: 8px; font-size: 10px; height: 19px; }
  .contact-icon {
    width: 13px; height: 13px; border-radius: 50%; background: var(--white);
    display: flex; align-items: center; justify-content: center; flex: none;
  }
  .contact-icon svg { width: 8px; height: 8px; }

  .address {
    position: absolute; right: 30px; top: 220px; text-align: right;
    color: var(--white); font-size: 10px; line-height: 1.6; letter-spacing: .3px;
  }

  .card--brand .brand-block { position: absolute; left: 0; right: 0; top: 60px; }
  .card--brand .brand-name { font-size: 26px; color: var(--white); }
  .card--brand .brand-dot { width: 52px; height: 52px; background: var(--white); margin-bottom: 12px; }
  .services {
    position: absolute; left: 24px; right: 24px; bottom: 30px;
    text-align: center; font-size: 10px; line-height: 1.8; color: var(--white);
  }
  .services span::before { content: "● "; font-size: 7px; vertical-align: 1px; }
  .services span { margin: 0 4px; white-space: nowrap; }
</style>
</head>
<body>

<section class="card card--contact" aria-label="Business card, contact side">
  <svg class="card__waves" viewBox="0 0 540 310" preserveAspectRatio="none" aria-hidden="true">
    <path d="M0,128 C140,100 300,170 540,122 L540,148 C300,192 140,126 0,150 Z" fill="var(--grey-wave)"/>
    <path d="M0,150 C150,126 300,196 540,150 L540,310 L0,310 Z" fill="var(--blue-mid)"/>
    <path d="M0,160 C150,136 300,206 540,160" fill="none" stroke="var(--white)" stroke-width="1.5" opacity=".6"/>
    <path d="M0,200 C180,170 330,250 540,200 L540,310 L0,310 Z" fill="var(--blue-deep)" opacity=".35"/>
  </svg>

  <div class="person">
    <p class="person__name">MARCUS DELANEY</p>
    <p class="person__role">OPERATIONS DIRECTOR</p>
  </div>

  <p class="brand-name"><span class="brand-dot"></span>HARBOURLINE<br>AGENTS LTD.</p>

  <ul class="contact-list">
    <li><span class="contact-icon"><svg viewBox="0 0 10 10"><path d="M2 1 L4 1 L4.6 3 L3.5 4 Q4.5 6 6 6.5 L7 5.4 L9 6 L9 8 Q5 9 1 4 Z" fill="var(--blue-mid)"/></svg></span>(242) 555-0147 (OFFICE)</li>
    <li><span class="contact-icon"><svg viewBox="0 0 10 10"><path d="M2 1 L4 1 L4.6 3 L3.5 4 Q4.5 6 6 6.5 L7 5.4 L9 6 L9 8 Q5 9 1 4 Z" fill="var(--blue-mid)"/></svg></span>(242) 555-0283 (CELL)</li>
    <li><span class="contact-icon"><svg viewBox="0 0 10 10"><rect x="1" y="2.5" width="8" height="5" fill="none" stroke="var(--blue-mid)" stroke-width="1"/><path d="M1 2.5 L5 5.5 L9 2.5" fill="none" stroke="var(--blue-mid)" stroke-width="1"/></svg></span>imports@harbourlineagents.com</li>
    <li><span class="contact-icon"><svg viewBox="0 0 10 10"><circle cx="5" cy="5" r="3.6" fill="none" stroke="var(--blue-mid)" stroke-width="1"/><path d="M1.4 5 H8.6 M5 1.4 V8.6" stroke="var(--blue-mid)" stroke-width=".8"/></svg></span>www.harbourlineagents.com</li>
    <li><span class="contact-icon"></span>@harbourlineagents</li>
    <li><span class="contact-icon"></span>@harbourlineagents</li>
  </ul>

  <p class="address">#42 CORAL RIDGE ROAD<br>P.O. BOX SP-50214<br>NASSAU, BAHAMAS</p>
</section>

<section class="card card--brand" aria-label="Business card, brand and services side">
  <div class="brand-block">
    <p class="brand-name"><span class="brand-dot"></span>HARBOURLINE<br>AGENTS LTD.</p>
  </div>
  <p class="services">
    <span>Import customs clearance</span><span>Delivery &amp; Handling services</span><span>Florida pickups</span><br>
    <span>Export packing &amp; Crating Services</span><span>Export customs clearance</span><span>Consulting</span>
  </p>
</section>

</body>
</html>
```